Sun Petal Custom Spray Tanning Studio

I have attached most of the information that I would like in my brochure. However, I would like the brochure to be more elegant and professional. I am no longer offering mobile tanning, however, I will be located at: 418 W Larkin Street, Myrtle Beach, SC 29577. 843-271-5046 and I am by appointment only.

Reason: I found designs that I like, however: Spelling and grammar is critical. Please make sure that every word is spelled correctly. I am also changing my colors with my new business cards.

Target Market(s)

My clients have an average to above average income. They are health conscience and take good care of themselves. Into high end quality work and willing to pay for it.

Industry/Entity Type

It Professional

Font styles to use
Serif
Decorative
Script

Requirements
Must have
• Correct Spelling and grammar are a must. Please make sure everything is spelled correctly, punctuated properly and words are used exactly like I have it my brochure.
Nice to have
• Elegant and Classy
Should not have
• Nothing to do with Mobile Tanning.
On the front, I prefer the wording.... Call and Make your appointments at (843)271-5046. Visit us online at www.sunpetalbronze.com or email me at maribel@sunpetalbronze.com

```html
<!DOCTYPE html>
<html lang="en">
<head>
<meta charset="utf-8">
<title>Sun Petal – Custom Sunless Tanning Brochure</title>
<link rel="stylesheet" href="https://fonts.googleapis.com/css2?family=Arimo:wght@400;700&family=Cormorant+Garamond:wght@600&family=Kaushan+Script&family=Pinyon+Script&display=swap">
<style>
  :root {
    --gold-light: #f6e6a6;
    --gold-mid: #d9b35c;
    --gold-deep: #a87a2c;
    --brown: #6b4530;
    --brown-dark: #4a2316;
    --ink: #231a10;
    --script-blue: #3a5fb0;
    --white: #ffffff;
    --pool: #3aa3cf;
    --skin: #c98a5c;
  }
  * { box-sizing: border-box; margin: 0; padding: 0; }
  html, body { width: 1200px; height: 927px; overflow: hidden; background: #fff; }
  .brochure {
    position: relative; width: 1200px; height: 927px; overflow: hidden;
    font-family: "Arimo", Arial, sans-serif; color: var(--ink);
  }
  .panel { position: absolute; top: 0; height: 927px; width: 400px; }
  .panel--left {
    left: 0;
    background: linear-gradient(160deg, var(--gold-deep) 0%, var(--gold-mid) 35%, var(--gold-light) 70%, var(--gold-mid) 100%);
  }
  .panel--middle {
    left: 400px;
    background: linear-gradient(120deg, var(--gold-mid) 0%, var(--gold-light) 45%, var(--gold-mid) 75%, var(--gold-deep) 100%);
    border-left: 1px dashed rgba(255,255,255,0.35);
  }
  .panel--right {
    left: 800px;
    background: linear-gradient(200deg, var(--gold-mid) 0%, var(--gold-light) 35%, var(--gold-mid) 65%, var(--gold-deep) 100%);
    border-left: 1px dashed rgba(255,255,255,0.35);
  }

  /* Left panel */
  .pool-photo {
    position: absolute; left: 0; top: 0; width: 400px; height: 380px;
    background: linear-gradient(180deg, var(--pool) 0%, #59b8dc 60%, rgba(217,179,92,0) 100%);
  }
  .body-text {
    position: absolute; left: 43px; width: 316px;
    font-size: 13px; line-height: 16.5px; font-weight: 700; color: var(--ink);
  }
  .intro { top: 414px; }
  .care-text--prep { top: 565px; }
  .care-text--after { top: 726px; }
  .script-heading {
    position: absolute; left: 42px;
    font-family: "Kaushan Script", cursive; font-size: 30px; line-height: 36px; font-weight: 400;
    color: var(--white);
    text-shadow: 0 0 2px var(--script-blue), 0 0 3px var(--script-blue), 1px 1px 0 var(--script-blue);
  }
  .script-heading--prep { top: 524px; }
  .script-heading--after { top: 684px; }
  .studio-info {
    position: absolute; left: 43px; top: 836px; width: 316px;
    font-size: 13px; line-height: 17px; font-weight: 700; color: var(--brown-dark);
  }
  .studio-info__note { display: block; margin-top: 4px; color: var(--brown); text-transform: uppercase; letter-spacing: 0.5px; }

  /* Middle panel */
  .prices-title {
    position: absolute; left: 0; width: 400px; top: 40px; text-align: center;
    font-family: "Pinyon Script", cursive; font-size: 40px; color: var(--brown-dark); font-weight: 400;
  }
  .price-list {
    position: absolute; left: 38px; top: 93px; width: 324px; list-style: none;
    border-top: 1px dotted var(--brown);
  }
  .price-item {
    display: flex; justify-content: space-between; align-items: flex-start;
    padding: 11px 0 0 16px; border-bottom: 1px dotted var(--brown);
    font-size: 11.3px; line-height: 14.4px; font-weight: 700; text-transform: uppercase;
  }
  .price-item__desc { width: 222px; color: var(--ink); }
  .price-item__name { color: var(--brown); display: block; }
  .price-item__amount { width: 70px; color: var(--brown); }
  .middle-phone {
    position: absolute; left: 0; width: 400px; top: 838px; text-align: center;
    font-size: 39px; color: var(--brown);
  }

  /* Right panel */
  .brand-block {
    position: absolute; left: 40px; top: 100px; width: 318px; height: 185px;
    background: var(--brown-dark); border: 1px solid rgba(255,255,255,0.25);
    display: flex; flex-direction: column; align-items: center; justify-content: center;
  }
  .brand-name {
    font-family: "Cormorant Garamond", serif; font-weight: 600; font-size: 50px;
    color: var(--gold-mid); line-height: 1;
  }
  .brand-tagline {
    margin-top: 12px;
    font-family: "Cormorant Garamond", serif; font-weight: 600; font-size: 17px; color: var(--gold-mid);
  }
  .call-heading {
    position: absolute; left: 0; width: 400px; top: 358px; text-align: center;
    font-family: "Kaushan Script", cursive; font-size: 29px; line-height: 33px; font-weight: 400;
    color: var(--white); text-shadow: 1px 1px 2px rgba(90,60,20,0.5);
  }
  .right-phone {
    position: absolute; left: 0; width: 400px; top: 433px; text-align: center;
    font-size: 39px; color: var(--brown);
  }
  .lounge-photo {
    position: absolute; left: 0; top: 513px; width: 400px; height: 273px;
    background: linear-gradient(180deg, var(--skin) 0%, #b07850 60%, #e8dcc4 85%, #d9c9a8 100%);
  }
  .online-text {
    position: absolute; left: 0; width: 400px; top: 822px; text-align: center;
    font-family: "Kaushan Script", cursive; font-size: 18px; line-height: 22px; font-weight: 400;
    color: var(--white); text-shadow: 1px 1px 2px rgba(90,60,20,0.5);
  }
</style>
</head>
<body>
<main class="brochure">

  <section class="panel panel--left">
    <div class="pool-photo" role="img" aria-label="Photo of a woman in a striped bikini and straw hat lying by a blue pool"></div>
    <p class="body-text intro">For the optimal tanning experience, make sure you follow Sun Petal’s recommendations for preparation and aftercare. This will ensure you obtain the best results possible from your sunless tanning experience.</p>
    <h2 class="script-heading script-heading--prep">Preparation</h2>
    <p class="body-text care-text--prep">Shower, shave and exfoliate at least 1 day before you tan. Come in for your appointment with clean dry skin. No lotion, makeup or deodorant. Wear dark, loose clothes, nothing hugging your body as this will leave lines.</p>
    <h2 class="script-heading script-heading--after">Aftercare</h2>
    <p class="body-text care-text--after">Wait 8-10 hours before showering. Do not swim, use hot tubs or exercise which will cause you to sweat and could remove your sunless tanner. Hydrate your skin with moisturizer twice a day and drink plenty of water.</p>
    <p class="studio-info">418 W Larkin Street, Myrtle Beach, SC 29577<span class="studio-info__note">By Appointment Only</span></p>
  </section>

  <section class="panel panel--middle">
    <h2 class="prices-title">Prices</h2>
    <ul class="price-list">
      <li class="price-item" style="height:43px"><span class="price-item__desc">Sun Petal’s Bronze tanning solution.</span><span class="price-item__amount">$55.00</span></li>
      <li class="price-item" style="height:44px"><span class="price-item__desc">Sun Petal’s Clear tanning solution.</span><span class="price-item__amount">$60.00</span></li>
      <li class="price-item" style="height:44px"><span class="price-item__desc">Sun Petal’s Shimmer hydration elixir.</span><span class="price-item__amount">$55.00</span></li>
      <li class="price-item" style="height:57px"><span class="price-item__desc"><span class="price-item__name">Bridal Package</span>Includes 3 tanning sessions and $120.00 of free products.</span><span class="price-item__amount">$160.00</span></li>
      <li class="price-item" style="height:73px"><span class="price-item__desc"><span class="price-item__name">Tanning Parties</span>Party of six or more the hostess tans free. *Price does not include hostess.</span><span class="price-item__amount">$49.00</span></li>
      <li class="price-item" style="height:58px"><span class="price-item__desc"><span class="price-item__name">Party of ten or more</span>The hostess tans free. *Price does not include hostess.</span><span class="price-item__amount">$44.00</span></li>
      <li class="price-item" style="height:87px"><span class="price-item__desc"><span class="price-item__name">Party of fifteen or more.</span>The hostess tans free and receives the Beauty Box. *Price does not include the hostess.</span><span class="price-item__amount">$35.00</span></li>
      <li class="price-item" style="height:88px"><span class="price-item__desc"><span class="price-item__name">Pure Radiance</span>Treat yourself to our super-hydrating normalize elixir with a full body sunless tanning session.</span><span class="price-item__amount">$70.00</span></li>
      <li class="price-item" style="height:131px"><span class="price-item__desc"><span class="price-item__name">The Bomb</span>The ultimate sunless tanning session in one, which includes our super, hydrating normalize elixir with a full-body sunless tanning session, followed by our anti-aging elixir, skin-firming treatment.</span><span class="price-item__amount">$75.00</span></li>
      <li class="price-item" style="height:89px"><span class="price-item__desc"><span class="price-item__name">The Beauty Box</span>Petal on the Go, Extend (with or without shimmer), exfoliant, and a full-body sunless tanning session.</span><span class="price-item__amount">$140.00</span></li>
    </ul>
    <p class="middle-phone">(843)271-5046</p>
  </section>

  <section class="panel panel--right">
    <div class="brand-block">
      <span class="brand-name">Sun Petal</span>
      <span class="brand-tagline">~Custom Sunless Tanning~</span>
    </div>
    <p class="call-heading">Call And Make Your<br>Appointments At</p>
    <p class="right-phone">(843)271-5046</p>
    <div class="lounge-photo" role="img" aria-label="Photo of a tanned woman in a black bikini reclining on a white lounge"></div>
    <p class="online-text">Visit Us Online At<br>www.sunpetalbronze.com or<br>email me at maribel@sunpetalbronze.com</p>
  </section>

</main>
</body>
</html>
```